Elegant Financial Planning Business Card

Clear Harbour Wealth Advisory Pty Ltd requires an elegant business card that communicates simplicity, elegance and trust.
Attached card example of 'Dorvane' is very close to what I am looking for. Looking for black and white card.
Update 24/1/16: The attached Dorvane card is almost exactly what I am looking for. Although it is possible that alternative layouts may interest me, it is considerably more likely that I will proceed with a virtual clone of the "Dorvane' example.
Industry/Entity Type
Financial Planning
Contact Information for Business Card
In black font...
Front Details are (layout as per Paula Dorvane card picture):
Line1 - Name: Simon Walsh
Line 2 - Company: Clear Harbour Wealth Advisory Pty Ltd
Line 3 - Address: Marlow Court 3, Level 14, 58 Tennant Road, Bondi Junction NSW
Line 4
- Phone: 178 526
- Email: advice@chwa-example.com.au
- Site: www.chwa-example.com.au
Back details
1/ logo in position and dimensions as per attached layout
2. Bottom left (in smaller writing).
- Authorised Representative No. 517649
- Clear Harbour Wealth Advisory is a corporate authorised representative of Tidewell Capital Partners Pty Ltd
- ABN 47 318 602 154
- AFSL No. 390817

```html
<!DOCTYPE html>
<html lang="en">
<head>
<meta charset="utf-8">
<title>Clear Harbour Wealth Advisory – Business Card</title>
<link rel="stylesheet" href="https://fonts.googleapis.com/css2?family=Tinos:wght@400;700&display=swap">
<style>
  :root {
    --bg: #e9e7e4;
    --paper: #ffffff;
    --ink: #1c1c1c;
    --ink-soft: #444444;
    --rule: #555555;
    --night: #0b0b0b;
    --night-sheen: #2a2a2a;
    --light: #f2f2f2;
  }
  * { box-sizing: border-box; margin: 0; padding: 0; }
  html, body { width: 1200px; height: 913px; overflow: hidden; }
  body {
    background: var(--bg);
    font-family: "Tinos", "Times New Roman", serif;
    color: var(--ink);
    position: relative;
  }
  .card {
    position: absolute;
    width: 560px;
    height: 320px;
    border-radius: 16px;
    box-shadow: 0 10px 28px rgba(0,0,0,0.18);
    overflow: hidden;
  }
  /* front */
  .card-front { left: 70px; top: 100px; background: var(--paper); }
  .front-rule {
    position: absolute; height: 1px; background: var(--rule);
  }
  .front-rule.top { left: 0; right: 0; top: 92px; }
  .front-rule.bottom { left: 120px; right: 0; top: 270px; }
  .brand {
    position: absolute; left: 150px; top: 40px; width: 200px;
    text-align: center;
  }
  .brand-mark {
    display: inline-block;
    font-size: 34px; font-weight: 400; line-height: 1;
    background: var(--paper); padding: 0 10px;
  }
  .brand-name {
    margin-top: 18px;
    font-size: 17px; letter-spacing: 1.5px; line-height: 1;
    color: var(--ink-soft);
  }
  .brand-sub {
    margin-top: 3px;
    font-size: 11px; letter-spacing: 0.6px; color: var(--ink-soft);
  }
  .person {
    position: absolute; left: 150px; top: 160px; width: 200px; text-align: center;
  }
  .person-name { font-size: 22px; font-weight: 700; }
  .person-role {
    margin-top: 2px; font-size: 12px; color: var(--ink-soft);
    display: flex; align-items: center; gap: 6px; justify-content: center;
  }
  .person-role::before, .person-role::after {
    content: ""; width: 34px; height: 1px; background: var(--rule);
  }
  .contact {
    position: absolute; left: 362px; top: 128px; list-style: none;
    font-size: 12.5px; line-height: 1.75; color: var(--ink);
  }
  .contact li { display: flex; align-items: center; gap: 7px; }
  .contact svg { width: 11px; height: 11px; flex: none; }
  .address {
    position: absolute; left: 150px; top: 226px; width: 240px;
    font-size: 13px; font-weight: 700; line-height: 1.4; text-align: center;
  }
  /* back */
  .card-back {
    left: 570px; top: 490px;
    background: linear-gradient(115deg, var(--night) 0%, var(--night) 40%, var(--night-sheen) 55%, var(--night) 70%, var(--night) 100%);
    color: var(--light);
  }
  .back-brand {
    position: absolute; right: 46px; top: 46px;
    font-size: 40px; font-weight: 400; line-height: 1; color: var(--light);
  }
  .legal {
    position: absolute; left: 40px; bottom: 34px; width: 440px;
    font-size: 12px; line-height: 1.45; color: var(--light);
  }
  .legal .ids { margin-bottom: 4px; }
</style>
</head>
<body>
  <section class="card card-front" aria-label="Business card front">
    <div class="front-rule top"></div>
    <div class="brand">
      <span class="brand-mark">Clear Harbour</span>
      <p class="brand-name">CLEAR HARBOUR</p>
      <p class="brand-sub">Wealth Advisory Pty Ltd</p>
    </div>
    <div class="person">
      <h1 class="person-name">Simon Walsh</h1>
      <p class="person-role">Director</p>
    </div>
    <ul class="contact">
      <li>
        <svg viewBox="0 0 12 12" aria-hidden="true"><path d="M2.2 1h2l1 2.6-1.3 1a6.5 6.5 0 0 0 3.5 3.5l1-1.3 2.6 1v2A1.2 1.2 0 0 1 9.8 11 9 9 0 0 1 1 2.2 1.2 1.2 0 0 1 2.2 1z" fill="#1c1c1c"/></svg>
        178 526
      </li>
      <li>
        <svg viewBox="0 0 12 12" aria-hidden="true"><rect x="0.8" y="2.2" width="10.4" height="7.6" fill="none" stroke="#1c1c1c" stroke-width="1.2"/><path d="M1 2.6 6 6.6 11 2.6" fill="none" stroke="#1c1c1c" stroke-width="1.2"/></svg>
        advice@chwa-example.com.au
      </li>
      <li>
        <svg viewBox="0 0 12 12" aria-hidden="true"><circle cx="6" cy="6" r="5.2" fill="none" stroke="#1c1c1c" stroke-width="1.1"/><ellipse cx="6" cy="6" rx="2.2" ry="5.2" fill="none" stroke="#1c1c1c" stroke-width="1"/><path d="M0.8 6h10.4M1.6 3.4h8.8M1.6 8.6h8.8" stroke="#1c1c1c" stroke-width="0.9"/></svg>
        www.chwa-example.com.au
      </li>
    </ul>
    <p class="address">Marlow Court 3, Level 14, 58<br>Tennant Road, Bondi Junction NSW</p>
    <div class="front-rule bottom"></div>
  </section>

  <section class="card card-back" aria-label="Business card back">
    <p class="back-brand">Clear Harbour</p>
    <div class="legal">
      <p class="ids">ABN 47 318 602 154<br>AFSL No. 390817</p>
      <p>Authorised Representative No. 517649<br>
      Clear Harbour Wealth Advisory is a corporate authorised<br>
      representative of Tidewell Capital Partners Pty Ltd</p>
    </div>
  </section>
</body>
</html>
```